Business Card Design

We need a new business card design for our company, Lumen Forge.

Our website: www.brightrow7.ca

We are open to all ideas, from professional to very creative.
Updates

Design update requests:

1. We would like to see some examples with "BrightRow7" instead of "Lumen Forge" as the company name.
2. Would like to see "Software | Web | Branding" included on the card somewhere as well.

Thanks.

We are really trying to express the nature of our business through our business card.  "Lumen" can be misconstrued for the health industry, so use of "BrightRow7" and the "Software | Web | Branding" slogan are key to understanding our business.

We have uploaded a new PSD which includes a monitor, tablet, and phone screen.  This represents the flexibility of web applications and is another tool we would like to see used on business cards.

We will be eliminating designs today and will await updated designs with these new specs.

Thank-you.

Industry/Entity Type

Business

Requirements
Must have
• Content:
First M. Last
Managing Partner
e. email@brightrow7.ca
p. 555.555.5555

```html
<!DOCTYPE html>
<html lang="en">
<head>
<meta charset="utf-8">
<title>BrightRow7 Business Card</title>
<link rel="stylesheet" href="https://fonts.googleapis.com/css2?family=Quicksand:wght@500;600;700&display=swap">
<style>
  :root {
    --backdrop: #4a3328;
    --card-white: #f4f4f4;
    --card-grey: #dcdcdc;
    --brand-blue: #2b6685;
    --brand-blue-light: #35718f;
    --tick-white: #ffffff;
  }
  * { margin: 0; padding: 0; box-sizing: border-box; }
  html, body {
    width: 1200px; height: 1181px; overflow: hidden;
    background: var(--backdrop);
    font-family: "Quicksand", sans-serif;
  }
  .card {
    position: absolute; left: 238px; width: 724px; height: 417px;
    border-radius: 20px; overflow: hidden;
    background: radial-gradient(ellipse at 50% 45%, #ffffff 0%, var(--card-white) 45%, var(--card-grey) 100%);
  }
  .card--front { top: 138px; }
  .card--back { top: 618px; }
  .ticked-edge {
    position: absolute; left: 0; right: 0; height: 14px;
    background:
      repeating-linear-gradient(90deg, transparent 0 20px, var(--tick-white) 20px 22px) 12px 3px / calc(100% - 24px) 8px no-repeat,
      var(--brand-blue);
  }
  .ticked-edge--top { top: 0; }
  .ticked-edge--bottom { bottom: 0; }
  .web-address {
    position: absolute; right: 6px; top: 50%;
    transform: translateY(-50%) rotate(-90deg) translateX(0);
    transform-origin: center;
    writing-mode: vertical-rl; transform: translateY(-50%) rotate(180deg);
    color: var(--brand-blue); font-size: 14px; font-weight: 700; letter-spacing: 0.5px;
  }
  .company-name {
    position: absolute; left: 0; right: 0; top: 165px;
    text-align: center; color: var(--brand-blue);
    font-size: 78px; font-weight: 700; letter-spacing: 1px;
  }
  .tagline {
    position: absolute; left: 0; right: 0; bottom: 18px;
    text-align: center; color: var(--brand-blue);
    font-size: 17px; font-weight: 600; letter-spacing: 0.3px;
  }
  .name-band {
    position: absolute; left: 0; right: 0; top: 95px; height: 227px;
    background: radial-gradient(ellipse at 50% 50%, var(--brand-blue-light) 0%, var(--brand-blue) 70%);
    color: #ffffff; text-align: center;
  }
  .person-name {
    position: absolute; left: 0; right: 0; top: 78px;
    font-size: 38px; font-weight: 600; letter-spacing: 1px;
  }
  .person-title {
    position: absolute; left: 0; right: 0; top: 122px;
    font-size: 21px; font-weight: 600; letter-spacing: 0.8px;
  }
  .card--back .web-address { color: #ffffff; }
  .contact-line {
    position: absolute; left: 0; right: 0; bottom: 18px;
    text-align: center; color: var(--brand-blue);
    font-size: 17px; font-weight: 600; letter-spacing: 0.3px;
  }
  .contact-line .divider { margin: 0 10px; }
</style>
</head>
<body>
  <section class="card card--front">
    <div class="ticked-edge ticked-edge--top"></div>
    <div class="company-name">BrightRow7</div>
    <div class="web-address">www.brightrow7.ca</div>
    <div class="tagline">Software | Web | Branding</div>
    <div class="ticked-edge ticked-edge--bottom"></div>
  </section>

  <section class="card card--back">
    <div class="ticked-edge ticked-edge--top"></div>
    <div class="name-band">
      <div class="person-name">First M. Last</div>
      <div class="person-title">Managing Partner</div>
    </div>
    <div class="web-address">www.brightrow7.ca</div>
    <div class="contact-line">555.555.5555<span class="divider">|</span>email@brightrow7.ca</div>
    <div class="ticked-edge ticked-edge--bottom"></div>
  </section>
</body>
</html>
```